Established food business needs a new name card design

Refer to attached current name card. Would like a new professional look design with only the company name and logo without any pictures. Would like green and yellow to be included.
To include:
My name "IBRAHIM SUKRI" and hand phone number "87260413".
To delete "
"Along Brackendale Ave 8" and
"www.nur-tiwas.com.sg"
To change email to:
"tkr27@velmorix.com.sg"

```html
<!DOCTYPE html>
<html lang="en">
<head>
<meta charset="utf-8">
<title>NUR-TIWAS Eating Corner – Name Card</title>
<link rel="stylesheet" href="https://fonts.googleapis.com/css2?family=Comic+Neue:wght@400;700&family=Questrial&display=swap">
<style>
  :root {
    --backdrop: #1c1c1c;
    --card-green-dark: #0d4a30;
    --card-green: #11583a;
    --card-green-light: #156a45;
    --brand-yellow: #f4ef06;
    --ink-white: #ffffff;
    --faint-mark: rgba(255, 255, 255, 0.06);
  }
  * { box-sizing: border-box; margin: 0; padding: 0; }
  html, body { width: 1200px; height: 1200px; overflow: hidden; }
  body {
    background: var(--backdrop);
    font-family: "Comic Neue", "Comic Sans MS", cursive;
    position: relative;
  }
  .card {
    position: absolute;
    left: 160px;
    width: 880px;
    height: 503px;
    border-radius: 34px;
    background: linear-gradient(135deg, var(--card-green-dark) 0%, var(--card-green) 55%, var(--card-green-light) 100%);
    overflow: hidden;
  }
  .card--front { top: 70px; }
  .card--back { top: 627px; }

  .brand {
    position: absolute;
    display: flex;
    align-items: center;
    gap: 18px;
  }
  .brand__dot {
    width: 74px; height: 74px;
    border-radius: 50%;
    background: var(--brand-yellow);
    flex: none;
  }
  .brand__words { display: flex; flex-direction: column; }
  .brand__name {
    font-family: "Comic Neue", "Comic Sans MS", cursive;
    font-weight: 700;
    font-size: 68px;
    line-height: 1;
    color: var(--brand-yellow);
    letter-spacing: 1px;
  }
  .brand__tagline {
    font-family: "Questrial", sans-serif;
    font-size: 19px;
    letter-spacing: 9px;
    color: var(--brand-yellow);
    border-bottom: 1.5px solid var(--brand-yellow);
    padding: 4px 0 4px 30px;
    margin-left: -30px;
  }
  .card--front .brand { left: 50%; top: 50%; transform: translate(-50%, -56%); }
  .card--back .brand { left: 70px; top: 56px; }
  .card--back .brand__dot { width: 66px; height: 66px; }
  .card--back .brand__name { font-size: 62px; }
  .card--back .brand__tagline { font-size: 17px; letter-spacing: 8px; }

  .watermark {
    position: absolute;
    right: -40px; top: 40px;
    width: 390px; height: 390px;
    border-radius: 50%;
    background: var(--faint-mark);
  }

  .holder {
    position: absolute;
    left: 60px; top: 258px;
    color: var(--ink-white);
  }
  .holder__name {
    font-weight: 700;
    font-size: 34px;
    letter-spacing: 2px;
    padding: 0 0 6px 8px;
  }
  .divider {
    position: absolute;
    left: 60px; right: 60px; top: 308px;
    height: 1.5px;
    background: var(--ink-white);
  }
  .contact {
    position: absolute;
    left: 60px; top: 322px;
    list-style: none;
    color: var(--ink-white);
    font-size: 23px;
    line-height: 32px;
  }
  .contact li { display: flex; align-items: center; gap: 14px; }
  .contact svg { width: 20px; height: 20px; fill: var(--brand-yellow); flex: none; }
  .address {
    position: absolute;
    right: 70px; bottom: 52px;
    text-align: right;
    color: var(--ink-white);
    font-size: 25px;
    line-height: 31px;
    font-style: normal;
  }
</style>
</head>
<body>
  <section class="card card--front" aria-label="Card front">
    <div class="brand">
      <span class="brand__dot"></span>
      <div class="brand__words">
        <span class="brand__name">NUR-TIWAS</span>
        <span class="brand__tagline">EATING CORNER</span>
      </div>
    </div>
  </section>

  <section class="card card--back" aria-label="Card back">
    <span class="watermark"></span>
    <div class="brand">
      <span class="brand__dot"></span>
      <div class="brand__words">
        <span class="brand__name">NUR-TIWAS</span>
        <span class="brand__tagline">EATING CORNER</span>
      </div>
    </div>
    <div class="holder"><p class="holder__name">IBRAHIM SUKRI</p></div>
    <span class="divider"></span>
    <ul class="contact">
      <li>
        <svg viewBox="0 0 24 24" aria-hidden="true"><path d="M6.6 10.8a15.1 15.1 0 0 0 6.6 6.6l2.2-2.2c.3-.3.7-.4 1-.2 1.1.4 2.3.6 3.6.6.6 0 1 .4 1 1V20c0 .6-.4 1-1 1A17 17 0 0 1 3 4c0-.6.4-1 1-1h3.5c.6 0 1 .4 1 1 0 1.3.2 2.5.6 3.6.1.3 0 .7-.2 1z"/></svg>
        <span>87260413</span>
      </li>
      <li>
        <svg viewBox="0 0 24 24" aria-hidden="true"><path d="M2 5h20v14H2zm2 2v.4l8 5 8-5V7zm0 2.8V17h16V9.8l-8 5z"/></svg>
        <span>tkr27@velmorix.com.sg</span>
      </li>
    </ul>
    <address class="address">
      18 Kelvara Industrial<br>
      Estate Road 2 # 02-07<br>
      Singapore 735418
    </address>
  </section>
</body>
</html>
```